HOT TUB - SPAS service needs an business card

I need an business for my company who his specialise in a maintenance,water treatment and cleaning of Hot Tub - Spas for commercial and residential customers. The company operate mainly in the ski resort of Chamonix, Megève and St Gervais. The final product should communicate pure water, cleanest and professional for luxury property's.
I have upload a logo but any improvement on it is welcome.(color,size, details etc..) or any other idea. Thank you
Company Name: 58 BAINS
My name: Laurent Mazeyrac
Email: lmazey@courrielo.fr
Tel: +33 (0)6 81 52 29 07
Description to be on the card in french(first langage) and in English:
- Spas service
- Entretien, traitement eau, nettoyage.
- Maintenance, water treatment, cleaning.

```html
<!DOCTYPE html>
<html lang="fr">
<head>
<meta charset="utf-8">
<title>58 BAINS – Business card</title>
<link href="https://fonts.googleapis.com/css2?family=Arimo:wght@400&display=swap" rel="stylesheet">
<style>
  :root {
    --backdrop: #d9d5d0;
    --card-front: #f5f5f5;
    --card-back: #e8e8e9;
    --brand-blue: #6a95cf;
    --ink-blue: #4d6ea9;
    --rule-blue: #4a68a6;
    --shadow: rgba(40, 30, 20, 0.28);
  }
  * { box-sizing: border-box; margin: 0; padding: 0; }
  html, body {
    width: 1200px;
    height: 848px;
    overflow: hidden;
  }
  body {
    position: relative;
    background: var(--backdrop);
    font-family: "Arimo", "Helvetica Neue", Arial, sans-serif;
  }
  .card {
    position: absolute;
    left: 321px;
    width: 552px;
    height: 338px;
    border-radius: 20px;
    box-shadow: 0 3px 8px var(--shadow);
  }
  .card--front { top: 37px; background: var(--card-front); }
  .card--back  { top: 471px; background: var(--card-back); }

  .brand {
    position: absolute;
    left: 0;
    right: 0;
    top: 0;
    bottom: 0;
    display: flex;
    align-items: center;
    justify-content: center;
    gap: 18px;
  }
  .brand__mark {
    width: 30px;
    height: 30px;
    background: var(--brand-blue);
  }
  .brand__name {
    color: var(--brand-blue);
    font-size: 54px;
    line-height: 1;
    font-weight: 400;
    letter-spacing: 1px;
    white-space: nowrap;
  }

  .services {
    position: absolute;
    left: 0;
    right: 0;
    top: 94px;
    list-style: none;
  }
  .services__item {
    display: flex;
    align-items: center;
    height: 30px;
    color: var(--ink-blue);
    font-size: 22px;
    white-space: nowrap;
  }
  .services__item::before,
  .services__item::after {
    content: "";
    flex: 1;
    height: 2px;
    background: var(--rule-blue);
  }
  .services__item span { padding: 0 8px; }

  .contact {
    position: absolute;
    left: 0;
    right: 0;
    top: 262px;
    text-align: center;
    color: var(--ink-blue);
  }
  .contact__name {
    font-size: 19px;
    letter-spacing: 0.3px;
    text-transform: uppercase;
    margin-bottom: 6px;
  }
  .contact__line {
    font-size: 15.5px;
    line-height: 20px;
  }
</style>
</head>
<body>
  <section class="card card--front">
    <div class="brand">
      <div class="brand__mark"></div>
      <div class="brand__name">58 BAINS</div>
    </div>
  </section>

  <section class="card card--back">
    <ul class="services">
      <li class="services__item"><span>Spas service</span></li>
      <li class="services__item"><span>Entretien, traitement eau, nettoyage</span></li>
      <li class="services__item"><span>Maintenance, water treatment, cleaning</span></li>
    </ul>
    <div class="contact">
      <p class="contact__name">Laurent Mazeyrac</p>
      <p class="contact__line">Email: lmazey@courrielo.fr</p>
      <p class="contact__line">Tel: +33 (0)6 81 52 29 07</p>
    </div>
  </section>
</body>
</html>
```